LUMA VelnoBloom MOISTURIZER LABEL

A revamp for a label design for our new product and bottles beauty products A canadian product with canadian sourced natural and organic ingredients looking for a bold playful Boutique fresh design i will provide our curent artwork for guidance but looking for similar with fruit splashing in water and clean and simple eye catching please! Front and back label size is 1 3/4 inch by 5 1/2 inch or 4.5 cm by 14 cm 8oz 240 ml its hypoallergenic and noncomedogenic which is important to note with omeg 3 6 9 and vitamins A C E K Coq10 and hyraulonic acid it is papya mango with bar code on back bottom would like the back to follow similar design to front with some slight changes an example would be to look at my old artwork and keep in mind new logo!
can also write on back contains organic ingredients

no GMOs, parabens, sulfates or preservatives, artificial flavors or fragrances, phthalates or animal testing doesn't have to be big

ingredientlist as follows

Distilled water
Kendrime organic hempseed oil, steric Acid, Olive oil, Shea nut butter, cetyl alcohol; Argan oil, carrot see oil, CoQ-10, Tavisol, Vitamin E, Hyaluronic acid, fragrance

also just waiting for for approval for 2 charity symbols which I provided work to establish ecologically sustainable communities First Nations will provide later lmk if any suggestions thank you and good luck!
Updates

Went on vacation/holiday

Target Market(s)

people looking for high quality natural organic product responsibly sourced

Industry/Entity Type

Health Product

Colors

Requirements
Must have
• fruit splashing in water eye catching refreshing fun modern good eye catching fonts and colour scheme white background or a mix of white with transparent

```html
<!DOCTYPE html>
<html lang="en">
<head>
<meta charset="utf-8">
<title>LUMA VelnoBloom Moisturizer Label</title>
<link rel="stylesheet" href="https://fonts.googleapis.com/css2?family=Pathway+Gothic+One&family=Cinzel+Decorative:wght@400&display=swap">
<style>
  :root {
    --page: #ffffff;
    --brand-blue: #1470b8;
    --brand-green: #6cbf3b;
    --water-light: #7fdcf6;
    --water-mid: #2ec2ee;
    --water-deep: #1a7fc4;
    --fruit-orange: #f08a1c;
    --fruit-red: #e0483a;
    --white: #ffffff;
  }
  html, body {
    margin: 0;
    width: 1200px;
    height: 1200px;
    overflow: hidden;
    background: var(--page);
  }
  .canvas {
    position: relative;
    width: 1200px;
    height: 1200px;
  }
  .label {
    position: absolute;
    left: 442px;
    top: 111px;
    width: 315px;
    height: 979px;
    background: var(--white);
    overflow: hidden;
    box-shadow: 0 0 3px rgba(0,0,0,0.12);
    font-family: "Pathway Gothic One", "Arial Narrow", sans-serif;
    text-align: center;
  }
  .brand {
    position: absolute;
    top: 28px;
    left: 0;
    width: 100%;
    display: flex;
    justify-content: center;
    align-items: center;
    gap: 8px;
  }
  .brand-mark {
    width: 14px;
    height: 14px;
    border-radius: 50%;
    background: var(--brand-green);
  }
  .brand-name {
    font-size: 54px;
    line-height: 1;
    color: var(--brand-green);
    letter-spacing: 2px;
  }
  .text-block {
    position: absolute;
    left: 0;
    width: 100%;
    margin: 0;
    color: var(--brand-blue);
  }
  .product-line { top: 131px; font-size: 32px; line-height: 34px; }
  .product-type { top: 165px; font-size: 33px; line-height: 34px; }
  .flavour {
    position: absolute;
    left: 0;
    width: 100%;
    font-family: "Cinzel Decorative", Georgia, serif;
    color: var(--brand-green);
    font-size: 50px;
    line-height: 60px;
    top: 196px;
    margin: 0;
  }
  .natural { top: 338px; font-size: 29px; line-height: 32px; }
  .nutrients {
    top: 380px;
    font-size: 17px;
    line-height: 25px;
    letter-spacing: 0.2px;
  }
  .free-from {
    top: 430px;
    font-size: 21px;
    line-height: 22.5px;
    padding: 0 40px;
    box-sizing: border-box;
  }
  .splash-art {
    position: absolute;
    left: 0;
    top: 545px;
    width: 100%;
    height: 434px;
    background:
      radial-gradient(ellipse 45% 30% at 30% 40%, var(--fruit-red) 0%, rgba(224,72,58,0) 100%),
      radial-gradient(ellipse 50% 35% at 70% 55%, var(--fruit-orange) 0%, rgba(240,138,28,0) 100%),
      linear-gradient(180deg, rgba(127,220,246,0) 0%, var(--water-light) 10%, var(--water-mid) 55%, var(--water-deep) 100%);
  }
  .volume {
    position: absolute;
    left: 22px;
    top: 893px;
    color: var(--white);
    font-size: 23px;
    line-height: 24px;
    text-align: center;
  }
  .badge {
    position: absolute;
    left: 218px;
    top: 883px;
  }
</style>
</head>
<body>
<div class="canvas">
  <section class="label">
    <div class="brand">
      <span class="brand-mark"></span>
      <span class="brand-name">LUMA</span>
    </div>
    <p class="text-block product-line">VelnoBloom</p>
    <p class="text-block product-type">MOISTURIZER</p>
    <h1 class="flavour">MANGO<br>PAPAYA</h1>
    <p class="text-block natural">100%NATURAL</p>
    <p class="text-block nutrients">OMEG 3 6 9 AND VITAMINS A C E K COQ10<br>AND HYRAULONIC ACID</p>
    <p class="text-block free-from">no GMOs, parabens, sulfates or preservatives, artificial flavors or fragrances, phthalates or animal testing doesn't have to be big</p>
    <div class="splash-art" role="img" aria-label="Mango and halved papaya splashing into clear blue water"></div>
    <p class="text-block volume">8oz<br>240 ml</p>
    <svg class="badge" width="76" height="76" viewBox="0 0 76 76" aria-hidden="true">
      <circle cx="38" cy="38" r="35" fill="none" stroke="var(--white)" stroke-width="3"/>
    </svg>
  </section>
</div>
</body>
</html>
```